Design a Framework Graphic for Our Online YouTube Course

We have created a system/framework to help teach our students one of our main concepts. We teach content creators and business owners how to grow on YouTube.
We made a rough outline of how we'd like the framework to look. So we'd at least like this made into a better image, cleaned up and made more cohesive. But we're also interested in seeing other creative ways of visualizing the framework. It could be designed in several different ways. Most important things are showing the process of going through each of these steps, and then repeating it over and over again.
1. Reverse Engineering
2. Research
3. Record
4. Release
5. Rocket - this is the pinnacle moment and we want to emphasize it
6. Review - (it's wrong on the attached image)
7. Repeat
The original vision was to show the first 3 steps as "ramping" up to the release time, then the rocket visual, then the rest is done and it circles back to step 1.
We want it to be something our students could print out an put on their wall. Something memorable that will help them memorize the system.
We also need an icon that can represent each step. The icon doesn't necessarily have to be on the master framework graphic, but we need these icons for use in the rest of our materials. We'd like simple, black and white graphic icons that represent each step.
Use the color red in the photo and we can send you the "Clip Summit Institute" logo if you need.
Target Market(s)
Beginner to advanced content creators and business owners who want to learn how to grow on YouTube
Font styles to use
Other font styles liked:
- Helvetica Neue is our brand font
Look and feel

```html
<!DOCTYPE html>
<html lang="en">
<head>
<meta charset="utf-8">
<title>Seven Step Growth Framework</title>
<link href="https://fonts.googleapis.com/css2?family=Arimo:wght@700&display=swap" rel="stylesheet">
<style>
  :root {
    --bg: #222224;
    --red: #e31e24;
    --white: #ffffff;
  }
  html, body {
    margin: 0;
    padding: 0;
    width: 1200px;
    height: 675px;
    overflow: hidden;
    background: var(--bg);
  }
  .framework {
    display: block;
    width: 1200px;
    height: 675px;
  }
  .loop-track {
    fill: none;
    stroke: var(--white);
    stroke-width: 9;
  }
  .step-pill { fill: var(--red); }
  .step-badge { fill: var(--white); }
  .step-number {
    fill: var(--red);
    font-family: "Arimo", "Helvetica Neue", Arial, sans-serif;
    font-weight: 700;
    font-size: 30px;
  }
  .step-label {
    fill: var(--white);
    font-family: "Arimo", "Helvetica Neue", Arial, sans-serif;
    font-weight: 700;
    font-size: 30px;
  }
  .icon-line {
    fill: none;
    stroke: var(--white);
    stroke-width: 5;
    stroke-linejoin: round;
    stroke-linecap: round;
    vector-effect: non-scaling-stroke;
  }
  .icon-accent {
    fill: none;
    stroke: var(--red);
    stroke-width: 5;
    stroke-linejoin: round;
    stroke-linecap: round;
    vector-effect: non-scaling-stroke;
  }
</style>
</head>
<body>
<svg class="framework" viewBox="0 0 1920 1080" xmlns="http://www.w3.org/2000/svg" role="img" aria-label="Seven step framework loop: Reverse Engineer, Research, Record, Release, Rocket, Review, Repeat">
  <defs>
    <g id="rocket-shape">
      <path class="icon-line" d="M1747,440 Q1750,420 1765,400 L1790,376 L1815,400 Q1830,420 1833,440 L1829,632 L1751,632 Z"/>
      <path class="icon-accent" d="M1748,443 Q1790,432 1832,443"/>
      <circle class="icon-accent" cx="1790" cy="489" r="28"/>
      <path class="icon-line" d="M1750,505 L1707,585 L1707,610 L1752,620"/>
      <path class="icon-line" d="M1830,505 L1873,585 L1873,610 L1828,620"/>
      <path class="icon-accent" d="M1765,642 L1815,642"/>
      <path class="icon-line" d="M1773,650 Q1762,680 1790,703 Q1818,680 1807,650"/>
      <path class="icon-accent" d="M1782,655 Q1778,675 1790,688 Q1802,675 1798,655"/>
    </g>
  </defs>

  <!-- loop -->
  <rect class="loop-track" x="360" y="290" width="1200" height="500" rx="80"/>

  <!-- steps -->
  <g class="step step-review">
    <rect class="step-pill" x="560" y="260" width="200" height="60" rx="16"/>
    <circle class="step-badge" cx="596" cy="290" r="20"/>
    <text class="step-number" x="596" y="301" text-anchor="middle">6</text>
    <text class="step-label" x="630" y="301">Review</text>
  </g>
  <g class="step step-rocket">
    <rect class="step-pill" x="1160" y="260" width="200" height="60" rx="16"/>
    <circle class="step-badge" cx="1196" cy="290" r="20"/>
    <text class="step-number" x="1196" y="301" text-anchor="middle">5</text>
    <text class="step-label" x="1230" y="301">Rocket</text>
  </g>
  <g class="step step-repeat">
    <rect class="step-pill" x="260" y="510" width="200" height="60" rx="16"/>
    <circle class="step-badge" cx="296" cy="540" r="20"/>
    <text class="step-number" x="296" y="551" text-anchor="middle">7</text>
    <text class="step-label" x="330" y="551">Repeat</text>
  </g>
  <g class="step step-release">
    <rect class="step-pill" x="1460" y="510" width="200" height="60" rx="16"/>
    <circle class="step-badge" cx="1496" cy="540" r="20"/>
    <text class="step-number" x="1496" y="551" text-anchor="middle">4</text>
    <text class="step-label" x="1530" y="551">Release</text>
  </g>
  <g class="step step-reverse-engineer">
    <rect class="step-pill" x="450" y="760" width="340" height="60" rx="16"/>
    <circle class="step-badge" cx="486" cy="790" r="20"/>
    <text class="step-number" x="486" y="801" text-anchor="middle">1</text>
    <text class="step-label" x="520" y="801">Reverse Engineer</text>
  </g>
  <g class="step step-research">
    <rect class="step-pill" x="920" y="760" width="225" height="60" rx="16"/>
    <circle class="step-badge" cx="956" cy="790" r="20"/>
    <text class="step-number" x="956" y="801" text-anchor="middle">2</text>
    <text class="step-label" x="990" y="801">Research</text>
  </g>
  <g class="step step-record">
    <rect class="step-pill" x="1275" y="760" width="195" height="60" rx="16"/>
    <circle class="step-badge" cx="1311" cy="790" r="20"/>
    <text class="step-number" x="1311" y="801" text-anchor="middle">3</text>
    <text class="step-label" x="1345" y="801">Record</text>
  </g>

  <!-- review icon: analytics monitor -->
  <g class="icon icon-review">
    <rect class="icon-line" x="550" y="62" width="220" height="144" rx="4"/>
    <rect class="icon-accent" x="558" y="71" width="204" height="125"/>
    <path class="icon-accent" d="M637,206 L637,216 M683,206 L683,216"/>
    <rect class="icon-line" x="625" y="216" width="70" height="11" rx="5"/>
    <rect class="icon-line" x="573" y="155" width="14" height="22"/>
    <rect class="icon-accent" x="592" y="120" width="14" height="57"/>
    <rect class="icon-line" x="611" y="142" width="14" height="35"/>
    <rect class="icon-accent" x="630" y="128" width="14" height="50"/>
    <rect class="icon-line" x="648" y="108" width="14" height="70"/>
    <polyline class="icon-line" points="580,113 600,97 620,106 658,87"/>
    <circle class="icon-accent" cx="714" cy="135" r="32"/>
    <path class="icon-line" d="M718,130 L718,102 A30,30 0 0 1 746,122 Z"/>
  </g>

  <!-- rocket icons -->
  <use href="#rocket-shape" class="icon icon-rocket" transform="translate(1262,143) rotate(45) scale(0.62) translate(-1790,-540)"/>
  <use href="#rocket-shape" class="icon icon-release"/>

  <!-- repeat icon -->
  <g class="icon icon-repeat">
    <path class="icon-line" d="M198,520 A72,58 0 0 0 66,512"/>
    <path class="icon-line" d="M46,514 L84,508 L62,536 Z"/>
    <path class="icon-accent" d="M62,560 A72,56 0 0 0 196,562"/>
    <path class="icon-accent" d="M214,562 L176,566 L200,542 Z"/>
  </g>

  <!-- reverse engineer icon -->
  <g class="icon icon-reverse-engineer">
    <path class="icon-line" d="M560,960 A72,72 0 1 1 700,960"/>
    <path class="icon-line" stroke-dasharray="14 10" d="M700,960 A72,72 0 0 1 566,975"/>
    <path class="icon-line" d="M538,950 L578,952 L560,972 Z"/>
    <circle class="icon-accent" cx="628" cy="948" r="30"/>
    <circle class="icon-accent" cx="628" cy="948" r="42"/>
    <circle class="icon-accent" cx="628" cy="948" r="48" stroke-width="12" stroke-dasharray="14 11"/>
  </g>

  <!-- research icon -->
  <g class="icon icon-research">
    <path class="icon-line" d="M958,875 L1040,875 L1073,908 L1073,1025 L958,1025 Z"/>
    <path class="icon-line" d="M1040,875 L1040,908 L1073,908"/>
    <rect class="icon-accent" x="970" y="958" width="12" height="20"/>
    <rect class="icon-line" x="988" y="945" width="12" height="33"/>
    <rect class="icon-accent" x="1006" y="938" width="14" height="40"/>
    <rect class="icon-line" x="1026" y="912" width="12" height="28"/>
    <rect class="icon-accent" x="1043" y="928" width="14" height="12"/>
    <path class="icon-line" d="M970,995 L1003,995 M1025,1005 L1058,1005"/>
    <path class="icon-accent" d="M970,1008 L1003,1008"/>
    <circle class="icon-line" cx="1048" cy="967" r="28"/>
    <path class="icon-line" stroke-width="12" d="M1070,990 L1098,1018"/>
  </g>

  <!-- record icon -->
  <g class="icon icon-record">
    <rect class="icon-line" x="1290" y="905" width="118" height="90" rx="10"/>
    <circle class="icon-line" cx="1350" cy="950" r="17"/>
    <path class="icon-line" d="M1410,935 L1455,913 L1455,985 L1410,963"/>
  </g>
</svg>
</body>
</html>
```